Retail Consultant Business Card Design

We're looking to update the look of our very old business cards. We work primarily in the fast paced retail industry, and would like a business card that won't look dated after a few years.

We are consultants that focus primarily on shopping malls (80%), or mixed use developments (20% shopping + office space + residential). That being the case, we know that there is a lot of room for creativity. We are not a law firm, so the design doesn't have to be very static or serious. We are also not a clothing brand, so it shouldn't be too "out there" (lipstick font, jean jacket background....etc).

We're looking for something more "middle of the road", with the design leaning more towards the creative side. Our consulting firm is not very big, so we are very open to breaking away from the "traditional" or simple business card model.

One last thing that might help you, is to know who we generally hand these cards out to. It really ranges from Developers to Architects, to actual retail brands like Vela, K&T, Brentwick, Tug & Fox, Lumira...etc.

Contact Information for Business Card

Company Name: (Horizon Venture Methods Worldwide, LLC)
Individuals Name & Title
Company Address: (382 W. Alder Lane, Suite C, Tustin, CA 92781)
Telephone Number: (714) 555-0182
Fax Number: (714) 555-0147
Website: hvmworld.example
Email

Font styles to use
Serif

Colors

Designer to choose colors to be used in the design.

Requirements
Must have
• 1. The incorporation of our logo in whatever way you think would work. We have no requirements for how this should happen.
• 2. Space in the back for a QR Code, with space for instructions like
• "save us as a contact on your mobile" (or something to that effect). This will allow our clients to scan the information on the card into their phones for quick contact creation. Obviously we will handle the whole QR Code issue, but if you could mock it up , so that we could get a sense of how it would look.
• 3. Try and use brighter colors, instead of darker ones. This is really up to you, the darker colors might make other colors pop. I just mention this, because we are trying to give the sense of energy or movement, if that makes any sense.
• 4. Obviously, space for all the normal business card text (Company name, person name, phone number, email.....etc)

```html
<!DOCTYPE html>
<html lang="en">
<head>
<meta charset="utf-8">
<title>Horizon Venture Methods Worldwide – Business Card</title>
<link rel="stylesheet" href="https://fonts.googleapis.com/css2?family=Source+Serif+4:opsz,wght@8..60,400;8..60,600;8..60,700&display=swap">
<style>
  :root {
    --backdrop: #b8b8b8;
    --card: #f4f4f4;
    --brand-blue: #1f86c9;
    --brand-orange: #e0731c;
    --ink: #2b2b2b;
    --ink-soft: #3a3a3a;
    --mark-tint: #d3e7f5;
    --qr-frame: #9fb3c2;
  }
  * { margin: 0; padding: 0; box-sizing: border-box; }
  html, body { width: 1200px; height: 576px; overflow: hidden; }
  body {
    position: relative;
    background: var(--backdrop);
    font-family: "Source Serif 4", Georgia, serif;
    color: var(--ink);
  }
  .card {
    position: absolute;
    top: 138px;
    height: 294px;
    background: var(--card);
    border-radius: 13px;
    overflow: hidden;
  }
  .card--front { left: 82px; width: 484px; }
  .card--back { left: 602px; width: 481px; }

  /* Front */
  .brand {
    position: absolute;
    left: 62px;
    top: 108px;
    display: flex;
    align-items: center;
    gap: 16px;
  }
  .brand__dot {
    width: 58px; height: 58px;
    border-radius: 50%;
    background: var(--brand-blue);
    flex: none;
  }
  .brand__name {
    font-weight: 600;
    font-size: 22px;
    line-height: 26px;
    color: var(--brand-blue);
  }
  .front__web {
    position: absolute;
    left: 0; right: 0;
    top: 240px;
    text-align: center;
    font-size: 14px;
    letter-spacing: 0.6px;
    color: var(--ink-soft);
  }
  .front__band {
    position: absolute;
    left: 0; right: 0; bottom: 0;
    height: 9px;
    display: flex;
  }
  .front__band span { flex: 1; }
  .front__band .band--blue { background: var(--brand-blue); }
  .front__band .band--orange { background: var(--brand-orange); }

  /* Back */
  .back__mark {
    position: absolute;
    left: 54px;
    top: 66px;
    width: 150px;
    height: 150px;
    border-radius: 50%;
    background: var(--mark-tint);
  }
  .contact {
    position: absolute;
    left: 269px;
    top: 50px;
  }
  .contact__name {
    font-weight: 700;
    font-size: 20px;
    line-height: 24px;
    color: var(--brand-blue);
  }
  .contact__title {
    font-size: 13px;
    line-height: 16px;
    color: var(--ink-soft);
    margin-bottom: 12px;
  }
  .contact__address {
    font-size: 13px;
    line-height: 17px;
    margin-bottom: 8px;
  }
  .contact__list { list-style: none; }
  .contact__list li {
    display: flex;
    align-items: center;
    font-size: 13px;
    line-height: 17px;
  }
  .contact__icon {
    width: 11px; height: 11px;
    margin: 0 14px 0 6px;
    fill: var(--brand-blue);
    flex: none;
  }
  .qr {
    position: absolute;
    left: 269px;
    top: 228px;
    display: flex;
    align-items: center;
    gap: 12px;
  }
  .qr__box {
    width: 46px; height: 46px;
    border: 1.5px dashed var(--qr-frame);
    background: #fff;
    flex: none;
  }
  .qr__note {
    font-size: 11px;
    line-height: 14px;
    color: var(--ink-soft);
  }
  .qr__note strong { color: var(--brand-blue); font-weight: 600; }
</style>
</head>
<body>

<section class="card card--front" aria-label="Card front">
  <div class="brand">
    <span class="brand__dot" aria-hidden="true"></span>
    <p class="brand__name">Horizon Venture Methods<br>Worldwide, LLC</p>
  </div>
  <p class="front__web">www.hvmworld.example</p>
  <div class="front__band" aria-hidden="true">
    <span class="band--blue"></span>
    <span class="band--orange"></span>
  </div>
</section>

<section class="card card--back" aria-label="Card back">
  <div class="back__mark" role="img" aria-label="Company mark area"></div>
  <div class="contact">
    <p class="contact__name">Marcus Lee Hart</p>
    <p class="contact__title">Managing Director</p>
    <p class="contact__address">382 W. Alder Lane, Suite C,<br>Tustin, CA 92781</p>
    <ul class="contact__list">
      <li>
        <svg class="contact__icon" viewBox="0 0 12 12" aria-label="Phone"><path d="M1 3.5C1 2 2.5 1 6 1s5 1 5 2.5V5H8.5V4h-5v1H1z"/><rect x="2.5" y="6" width="7" height="5" rx="1"/></svg>
        (714) 555-0182
      </li>
      <li>
        <svg class="contact__icon" viewBox="0 0 12 12" aria-label="Fax"><rect x="3" y="0.5" width="6" height="3"/><rect x="0.5" y="4" width="11" height="5" rx="1"/><rect x="3" y="7.5" width="6" height="4" fill="#fff"/></svg>
        (714) 555-0147
      </li>
      <li>
        <svg class="contact__icon" viewBox="0 0 12 12" aria-label="Website"><path d="M0.5 2.5h11v7h-11z"/><path d="M0.5 2.5L6 7l5.5-4.5" fill="none" stroke="#fff" stroke-width="1"/></svg>
        www.hvmworld.example
      </li>
      <li>
        <svg class="contact__icon" viewBox="0 0 12 12" aria-label="Email"><circle cx="6" cy="6" r="5.5"/><path d="M0.5 6h11M6 0.5v11M6 0.5c-3 3-3 8 0 11M6 0.5c3 3 3 8 0 11" fill="none" stroke="#fff" stroke-width="0.8"/></svg>
        name@hvmworld.example
      </li>
    </ul>
  </div>
  <div class="qr">
    <div class="qr__box" role="img" aria-label="QR code space"></div>
    <p class="qr__note"><strong>Scan me</strong> to save us as a<br>contact on your mobile</p>
  </div>
</section>

</body>
</html>
```